Business Card Design Project

we need a business card design for our company: www.plomvik.ch
It's important to include our already existing logo (see website)

```html
<!DOCTYPE html>
<html lang="en">
<head>
<meta charset="utf-8">
<title>Plomvik – Business Card</title>
<link rel="stylesheet" href="https://fonts.googleapis.com/css2?family=Arimo:wght@400;700&display=swap">
<style>
  :root {
    --stage: #000000;
    --card-blue: #2464b4;
    --card-blue-light: #2f76c8;
    --card-blue-deep: #1a4f96;
    --band: #14396f;
    --panel: #163e7a;
    --name: #9db9e2;
    --mark: #1f78d1;
    --ink: #ffffff;
  }
  html, body {
    margin: 0;
    padding: 0;
    width: 1200px;
    height: 900px;
    overflow: hidden;
    background: var(--stage);
  }
  .canvas {
    position: relative;
    width: 1200px;
    height: 900px;
    background: var(--stage);
    font-family: "Arimo", Arial, sans-serif;
  }
  .card {
    position: absolute;
    top: 227px;
    height: 377px;
    overflow: hidden;
  }
  .card--front { left: 7px; width: 588px; }
  .card--back  { left: 603px; width: 589px; }
  .card__texture {
    position: absolute;
    inset: 0;
    background:
      radial-gradient(ellipse at 30% 25%, var(--card-blue-light) 0%, transparent 60%),
      radial-gradient(ellipse at 70% 85%, var(--card-blue-light) 0%, transparent 55%),
      linear-gradient(180deg, var(--card-blue) 0%, var(--card-blue-deep) 50%, var(--card-blue) 100%);
  }
  .band {
    position: absolute;
    left: 0;
    right: 0;
    background: var(--band);
    display: flex;
    align-items: center;
  }
  .card--front .band { top: 130px; height: 105px; }
  .card--back .band--logo { top: 35px; height: 60px; }
  .card--back .band--contact {
    top: 141px;
    height: 182px;
    background: var(--panel);
    align-items: flex-start;
  }
  .brand {
    display: flex;
    align-items: center;
    color: var(--name);
    font-weight: 400;
    letter-spacing: -1px;
    line-height: 1;
  }
  .brand__mark {
    background: var(--mark);
    flex: none;
  }
  .card--front .brand { margin-left: 70px; font-size: 92px; }
  .card--front .brand__mark { width: 56px; height: 56px; margin-right: 18px; }
  .card--back .brand { margin-left: 17px; font-size: 56px; }
  .card--back .brand__mark { width: 34px; height: 34px; margin-right: 12px; }
  .contact {
    list-style: none;
    margin: 40px 0 0 74px;
    padding: 0;
    color: var(--ink);
    font-weight: 700;
    font-size: 21px;
    line-height: 25px;
  }
</style>
</head>
<body>
<main class="canvas">
  <section class="card card--front" aria-label="Card front">
    <div class="card__texture" role="img" aria-label="Blue textured card background"></div>
    <div class="band">
      <div class="brand"><span class="brand__mark"></span><span class="brand__name">Plomvik</span></div>
    </div>
  </section>

  <section class="card card--back" aria-label="Card back">
    <div class="card__texture" role="img" aria-label="Blue textured card background"></div>
    <div class="band band--logo">
      <div class="brand"><span class="brand__mark"></span><span class="brand__name">Plomvik</span></div>
    </div>
    <div class="band band--contact">
      <ul class="contact">
        <li>Telephone</li>
        <li>Address</li>
        <li>Email</li>
        <li>Website</li>
      </ul>
    </div>
  </section>
</main>
</body>
</html>
```